Poster Design Project

We are launching a new company Q Vyn, we sell advertising on digital signage and we are launching our company selling ads at our 2 locations, Marlow Bend Sports and Rec Club and the Tresgold Reef Sports and Rec Club. We want to advertise that we have 5 10 and 15 ad slots available and ads start from as little as $27.00 per week. We need to let people know we offer 10% discount to LWBTO members. it needs to have the following contact details to get more information, Gideon 0479352104 and gideon@qvyn.com.au. As a new launch we are offering for the first 10 customers one of 2 discounts, get 4 weeks free all you have to pay is the content creation fee ($99 for 5 second ad) or 4 weeks free and free content creation if you sign up to a 18 week contract.

Update: need the add to start wit something like this but you can be creative:

Need to get you message or brand out, Have you heard of digital sinage?
We have ads avaliable starting from $27 per week at one of our locations.

Or something like that, as i am introducing my company they dont know what i do you untill they read this poster.

Target Market(s)

Targeting small to medium buisness

Industry/Entity Type

Advertising

Requirements
Must have
• Logo

```html
<!DOCTYPE html>
<html lang="en">
<head>
<meta charset="utf-8">
<title>Q Vyn – Digital Signage Advertising</title>
<link href="https://fonts.googleapis.com/css2?family=Anton&family=Josefin+Sans:wght@400;600&family=Ubuntu:wght@400&display=swap" rel="stylesheet">
<style>
:root{
  --ink:#000;
  --white:#fff;
  --yellow:#fcdc2c;
  --yellow-band:#fde023;
  --sky:#5ac8de;
  --sky-text:#2aa6d8;
  --green:#0b6e4f;
  --dark:#111;
}
*{margin:0;padding:0;box-sizing:border-box}
html,body{width:927px;height:1200px;overflow:hidden;background:var(--ink)}
.poster{position:relative;width:927px;height:1200px;background:var(--ink);overflow:hidden;color:var(--white)}
.abs{position:absolute;white-space:nowrap}
.headline{font-family:"Anton",sans-serif;line-height:1;letter-spacing:1px}
.caps{font-family:"Josefin Sans",sans-serif;text-transform:uppercase;letter-spacing:1px}
.body{font-family:"Ubuntu",sans-serif}

.member-badge{position:absolute;left:0;top:0}
.member-offer{left:478px;top:48px;transform:rotate(8deg);transform-origin:left top;font-size:31px;line-height:1.08;color:var(--white)}
.member-offer .note{display:block;margin-left:128px;font-size:23px;color:var(--yellow);text-transform:none;letter-spacing:0}

.hook-1{left:44px;top:40px;font-size:100px}
.hook-2{left:44px;top:132px;font-size:100px}
.hook-3{left:106px;top:222px;font-size:108px;color:var(--yellow)}

.band{position:absolute;left:0;display:flex;align-items:center}
.band-signage{top:345px;width:927px;height:52px;background:var(--sky);justify-content:center;color:var(--dark);font-size:37px;padding-top:6px}
.tab-available{top:407px;width:310px;height:56px;background:var(--green);padding-left:34px;font-size:46px}

.slots{position:absolute;left:0;top:0}
.slots text{font-family:"Anton",sans-serif;fill:var(--sky)}
.slot-price{left:152px;top:592px;font-size:34px;line-height:1.15;transform:rotate(-5deg);text-align:center}

.first-ten{left:500px;top:403px;font-size:42px;letter-spacing:3px;color:var(--yellow)}
.get-discounts{left:556px;top:462px;font-size:40px;color:var(--sky)}
.offer-box{position:absolute;left:523px;width:404px;background:var(--white);color:var(--dark);text-align:right;padding:6px 24px 0 0;font-size:21px;line-height:1.2}
.offer-1{top:507px;height:65px}
.offer-2{top:579px;height:87px}

.band-locations{top:709px;width:863px;height:54px;background:var(--green);padding-left:34px;font-size:38px;padding-top:6px}
.locations{right:27px;top:777px;text-align:right;color:var(--sky);font-size:31px;line-height:1.15;letter-spacing:0.5px}

.cta-band{position:absolute;left:0;top:0}
.cta{left:56px;top:828px;font-size:94px;color:var(--ink);transform:rotate(7deg);transform-origin:left top}

.brand-square{position:absolute;left:44px;top:990px;width:112px;height:112px;background:var(--sky-text)}
.brand-name{left:184px;top:1032px;font-size:78px;color:var(--white)}

.contact{left:448px;top:972px;font-size:74px;transform:rotate(5deg);transform-origin:left top}
.contact-call{left:582px;top:1066px;font-size:28px;color:var(--sky-text);transform:rotate(5deg);transform-origin:left top;letter-spacing:1px}
.contact-email{left:402px;top:1100px;font-size:28px;color:var(--sky-text);transform:rotate(5deg);transform-origin:left top;letter-spacing:1px}
</style>
</head>
<body>
<main class="poster">
  <svg class="member-badge" width="927" height="260" viewBox="0 0 927 260" aria-hidden="true">
    <ellipse cx="680" cy="95" rx="285" ry="150" transform="rotate(8 680 95)" fill="var(--green)"/>
  </svg>
  <p class="abs caps member-offer">Special 10%discount<br>to LWBTO members<span class="note">Mention this poster</span></p>

  <h1 class="abs headline hook-1">LOOKING</h1>
  <p class="abs headline hook-2">TO ATTRACT</p>
  <p class="abs headline hook-3">MORE CUSTOMERS?</p>

  <div class="band band-signage caps">Advertise through digital signage</div>

  <div class="band tab-available headline">AVAILABLE</div>
  <svg class="slots" width="927" height="700" viewBox="0 0 927 700" aria-label="5, 10, 15">
    <text x="52" y="577" font-size="73">5,</text>
    <text x="103" y="592" font-size="146">10,</text>
    <text x="288" y="572" font-size="163">15</text>
  </svg>
  <p class="abs body slot-price">Ad Slots starting<br>at $27 per week</p>

  <p class="abs headline first-ten">FIRST 10 CUSTOMERS</p>
  <p class="abs caps get-discounts">Get discounts</p>
  <div class="offer-box body offer-1">4 weeks free, only pay for<br>content creation ($99)</div>
  <div class="offer-box body offer-2">4 weeks free and free<br>content creation if you sign<br>up to a 18 week contract.</div>

  <div class="band band-locations caps">At two convenient locations</div>
  <p class="abs body locations">&gt;Marlow Bend Sports &amp; Rec Club<br>&gt;The Tresgold Reef Sports<br>&amp; Rec Club</p>

  <svg class="cta-band" width="927" height="1200" viewBox="0 0 927 1200" aria-hidden="true">
    <polygon points="0,808 927,932 927,1020 0,896" fill="var(--yellow-band)"/>
  </svg>
  <p class="abs headline cta">SAVE A SPOT TODAY!!!</p>

  <div class="brand-square" aria-hidden="true"></div>
  <p class="abs headline brand-name">Q Vyn</p>

  <p class="abs headline contact">CONTACT GIDEON</p>
  <p class="abs body contact-call">CALL- 0479352104</p>
  <p class="abs body contact-email">EMAIL- gideon@qvyn.com.au</p>
</main>
</body>
</html>
```